RW Framewell Inc Business cards

We need business cards using our existing logo but slightly modified. Right now the logo says RW Bedrock Masonry. We want to keep the RW part of the design, but replace the Bedrock Masonry portion with "FRAMEWELL". Please see the attached file.
Ideally this would be a blank template so we can add Different Names, titles, and phone numbers later.
On the one side we want only the logo and on the other side the detail. I'm attaching an example for you to see.
Please reach out with any other questions. Our address and other details will be given out once we find a design we like.

Target Market(s)

Construction Industry

```html
<!DOCTYPE html>
<html lang="en">
<head>
<meta charset="UTF-8">
<title>RW Framewell Inc – Business Cards</title>
<link href="https://fonts.googleapis.com/css2?family=Montserrat:wght@700&family=Questrial&display=swap" rel="stylesheet">
<style>
  :root {
    --brand-blue: #0075c6;
    --brand-blue-deep: #0068b4;
    --steel-grey: #74767b;
    --text-grey: #5d6066;
    --card-white: #f3f3f4;
    --backdrop: #e2e2e3;
  }
  * { margin: 0; padding: 0; box-sizing: border-box; }
  html, body {
    width: 1200px; height: 900px; overflow: hidden;
    background: var(--backdrop);
  }
  .sheet { position: relative; width: 1200px; height: 900px; }
  .card {
    position: absolute; left: 250px; width: 700px; height: 400px;
    overflow: hidden;
  }
  .card--front { top: 30px; background: var(--brand-blue); }
  .card--back { top: 470px; background: var(--card-white); }

  .front-wordmark {
    position: absolute; inset: 0;
    display: flex; align-items: center; justify-content: center;
    font-family: "Montserrat", sans-serif; font-weight: 700;
    font-size: 64px; letter-spacing: 4px; color: #ffffff;
  }

  .back-wordmark {
    position: absolute; left: 33px; top: 76px;
    font-family: "Montserrat", sans-serif; font-weight: 700;
    font-size: 44px; letter-spacing: 2px; color: var(--brand-blue);
  }

  .holder {
    position: absolute; right: 40px; top: 182px; text-align: right;
  }
  .holder__name {
    font-family: "Montserrat", sans-serif; font-weight: 700;
    font-size: 29px; color: var(--brand-blue); line-height: 34px;
  }
  .holder__title {
    font-family: "Questrial", sans-serif; font-size: 18px; line-height: 22px;
    color: var(--text-grey); margin-top: 1px;
  }
  .holder-rule {
    position: absolute; left: 33px; top: 225px; width: 540px; height: 2px;
    background: var(--steel-grey);
  }
  .holder-tab {
    position: absolute; left: 683px; top: 195px; width: 17px; height: 38px;
    background: var(--steel-grey);
  }

  .contact-list {
    position: absolute; left: 33px; top: 246px; list-style: none;
    font-family: "Questrial", sans-serif; font-size: 18px; color: var(--text-grey);
  }
  .contact-list li { display: flex; align-items: center; height: 25px; }
  .contact-list svg { width: 16px; height: 16px; margin-right: 10px; flex: none; }

  .address {
    position: absolute; right: 40px; top: 276px; text-align: right;
    font-family: "Questrial", sans-serif; font-size: 18px; line-height: 20px;
    color: var(--text-grey);
  }

  .band { position: absolute; left: 0; width: 700px; }
  .band--grey { top: 334px; height: 8px; background: var(--steel-grey); }
  .band--blue { top: 350px; height: 50px; background: var(--brand-blue-deep); }
</style>
</head>
<body>
<main class="sheet">

  <section class="card card--front" aria-label="Card front">
    <div class="front-wordmark">RW FRAMEWELL</div>
  </section>

  <section class="card card--back" aria-label="Card back">
    <div class="back-wordmark">RW FRAMEWELL</div>

    <div class="holder">
      <div class="holder__name">JORDAN HALE</div>
      <div class="holder__title">FOUNDER</div>
    </div>
    <div class="holder-rule"></div>
    <div class="holder-tab"></div>

    <ul class="contact-list">
      <li>
        <svg viewBox="0 0 16 16" aria-hidden="true">
          <path d="M3.2 1.5l2.2 2.6-1.3 1.6c.9 2 2.4 3.6 4.3 4.5l1.6-1.3 2.6 2.2-1.2 2.2C6.5 13.1 2.6 9.3 1 4.4z" fill="var(--brand-blue)"/>
          <path d="M9.5 2.5a4.5 4.5 0 0 1 4 4M9.3 4.5a2.6 2.6 0 0 1 2.2 2.2" stroke="var(--brand-blue)" stroke-width="1.2" fill="none"/>
        </svg>
        +000000000000
      </li>
      <li>
        <svg viewBox="0 0 16 16" aria-hidden="true">
          <rect x="0.5" y="3" width="15" height="10" fill="var(--brand-blue)"/>
          <path d="M1 3.5l7 5.5 7-5.5M1 12.5l5-4.5M15 12.5l-5-4.5" stroke="#ffffff" stroke-width="1.2" fill="none"/>
        </svg>
        INFO@YOURMAIL.COM
      </li>
      <li>
        <svg viewBox="0 0 16 16" aria-hidden="true">
          <circle cx="8" cy="8" r="7" fill="none" stroke="var(--brand-blue)" stroke-width="1.4"/>
          <path d="M1 8h14M8 1c-2.5 2-2.5 12 0 14M8 1c2.5 2 2.5 12 0 14" stroke="var(--brand-blue)" stroke-width="1.2" fill="none"/>
        </svg>
        WWW.YOURWEBSITE.COM
      </li>
    </ul>

    <div class="address">YOUR LOCATION STREET<br>HERE UNITED STREET-9100</div>

    <div class="band band--grey"></div>
    <div class="band band--blue"></div>
  </section>

</main>
</body>
</html>
```